Mental Health care Company in Washington DC

We are a new mental health care services provider in Washington DC. Please look at these sites.
https://marlowbrookpartners.com
https://www.quillstoneinc.com
https://velmarsh-kt.org/
https://www.trivanqx.com
https://www.thelanternofqz.com

```html
<!DOCTYPE html>
<html lang="en">
<head>
<meta charset="utf-8">
<title>Velora Health Services — Mental Health Care in Washington DC</title>
<link href="https://fonts.googleapis.com/css2?family=Lexend:wght@400;500;600&family=Inter:wght@400;500;600&display=swap" rel="stylesheet">
<style>
:root{
  --navy:#102a43;
  --orange:#f37f23;
  --teal:#a5d9dc;
  --teal-soft:#d4eef0;
  --ink:#1b1b1b;
  --muted:#5d6670;
  --white:#ffffff;
  --line:#d9dee2;
  --footer:#5e6d79;
}
*{box-sizing:border-box;margin:0;padding:0}
html,body{width:1200px;height:4112px;overflow:hidden}
body{font-family:"Inter",Arial,sans-serif;color:var(--ink);background:var(--white);position:relative}
.abs{position:absolute}
h1,h2,h3,.lx{font-family:"Lexend",Arial,sans-serif;font-weight:500}
.btn{position:absolute;display:flex;align-items:center;justify-content:center;border-radius:20px;background:var(--navy);color:var(--white);font-size:13px;font-family:"Inter",Arial,sans-serif}
.btn.orange{background:var(--orange)}
.photo{position:absolute;border-radius:8px}
.brand{display:flex;align-items:center;gap:8px;font-family:"Lexend",Arial,sans-serif;font-weight:500;color:var(--navy)}
.brand .dot{width:12px;height:12px;border-radius:50%;background:var(--orange)}

/* hero */
.hero{position:absolute;left:0;top:0;width:1200px;height:704px}
.hero-photo{position:absolute;inset:0;background:linear-gradient(100deg,#f4f5f6 0%,#eef1f2 38%,#cfe4e6 58%,#e9e2d8 75%,#b9cf9c 100%)}
.nav{position:absolute;left:346px;top:29px;width:508px;height:38px;border-radius:19px;background:rgba(225,228,230,.85);display:flex;align-items:center;justify-content:space-around;font-size:13px;padding:0 12px}
.nav a{color:var(--ink);text-decoration:none}
.nav a.active{color:var(--orange);border-bottom:2px solid var(--orange);padding-bottom:2px}
.hero h1{position:absolute;left:64px;top:250px;font-size:42px;line-height:54px;color:var(--ink)}
.hero .sub{position:absolute;left:64px;top:366px;font-size:26px;font-family:"Lexend",Arial,sans-serif;font-weight:400}
.hero .lead{position:absolute;left:64px;top:420px;width:400px;font-size:11px;line-height:16px;color:var(--muted)}
.stat{position:absolute;background:rgba(235,238,240,.92);display:flex;align-items:center}
.stat .faces{display:flex}
.stat .faces span{width:30px;height:30px;border-radius:50%;background:linear-gradient(135deg,#9bb2bf,#5b6f7c);border:2px solid #fff;margin-left:-8px}
.stat-care{left:380px;top:527px;width:252px;height:68px;border-radius:34px;padding-left:40px;gap:18px}
.stat-care b{font-family:"Lexend",Arial,sans-serif;font-weight:400;font-size:26px;display:block;line-height:26px}
.stat-care small{font-size:9px;display:block;text-align:right}
.tick{position:absolute;left:594px;top:516px;width:22px;height:22px;border-radius:50%;background:var(--navy)}
.stat-doc{left:1021px;top:303px;width:115px;height:112px;border-radius:50%;flex-direction:column;justify-content:center}
.stat-doc b{font-family:"Lexend",Arial,sans-serif;font-weight:400;font-size:24px;line-height:24px}
.stat-doc small{font-size:8px}

/* about */
.eyebrow{font-family:"Lexend",Arial,sans-serif;font-weight:500;font-size:28px;letter-spacing:.5px}
.about .eyebrow{position:absolute;left:64px;top:820px}
.about h2{position:absolute;left:64px;top:874px;font-size:32px;line-height:44px}
.body-text{font-size:11.5px;line-height:20px;color:var(--ink)}

/* services */
.band{position:absolute;left:0;width:1200px;background:var(--teal)}
.band-title{position:absolute;left:0;width:1200px;text-align:center;color:var(--white);font-family:"Lexend",Arial,sans-serif;font-weight:400}
.svc{position:absolute;top:1628px;width:259px;height:420px;background:var(--white);border-radius:10px}
.svc .img{position:absolute;left:12px;top:26px;width:235px;height:174px;border-radius:8px 8px 14px 14px;border-bottom:14px solid var(--teal)}
.svc.featured .img{border-bottom-color:var(--orange)}
.svc .head{position:absolute;left:12px;top:220px;display:flex;align-items:center;gap:10px;font-size:18px}
.svc .icon{width:40px;height:40px;border-radius:50%;background:var(--teal-soft);display:flex;align-items:center;justify-content:center}
.svc .rule{position:absolute;left:0;top:271px;width:100%;height:1px;background:var(--line)}
.svc p{position:absolute;left:12px;top:290px;width:235px;font-size:11.5px;line-height:20px}
.svc .btn{left:12px;top:364px;width:103px;height:30px}

/* team */
.section-label{position:absolute;left:0;width:1200px;text-align:center;font-family:"Lexend",Arial,sans-serif}
.member{position:absolute;top:2325px;width:261px;height:286px;border:1.5px solid #c9cfd3;background:var(--white);text-align:center}
.member .band-top{position:absolute;left:0;top:0;width:100%;height:69px;background:linear-gradient(90deg,#c7e7e9,#e9f6f7)}
.member .avatar{position:absolute;left:82px;top:37px;width:96px;height:96px;border-radius:50%;background:linear-gradient(135deg,#e6eef2,#7ea7b8)}
.member h3{position:absolute;left:0;top:143px;width:100%;font-size:18px;font-weight:400}
.member p{position:absolute;left:20px;top:176px;width:221px;font-size:11.5px;line-height:20px}
.member .more{position:absolute;left:0;top:248px;width:100%;font-size:12px;color:var(--orange);display:flex;justify-content:center;align-items:center;gap:8px}

/* testimonials */
.review{position:absolute;top:2911px;width:441px;height:171px;background:var(--white);border-radius:14px;border:2px solid #e7f3f4}
.review p{position:absolute;left:16px;top:18px;width:300px;font-size:11.5px;line-height:20px;color:var(--muted)}
.review .who{position:absolute;left:16px;top:100px;display:flex;gap:14px;align-items:flex-start}
.review .pic{width:56px;height:56px;border-radius:50%;background:linear-gradient(135deg,#b8c2c9,#3f4a52)}
.review h4{font-family:"Lexend",Arial,sans-serif;font-weight:400;font-size:18px;margin-top:-2px}
.review small{display:block;font-size:10.5px;line-height:18px;color:var(--muted);margin-top:4px}
.stars{position:absolute;right:20px;top:130px;color:#f2a62a;font-size:14px;letter-spacing:6px}

/* contact */
.contact-box{position:absolute;left:120px;top:3361px;width:962px;height:305px;background:#f6f6f6}
.contact-info{position:absolute;left:0;top:0;width:301px;height:305px;background:var(--teal);border-radius:10px 0 0 10px;color:var(--white)}
.contact-info h5{position:absolute;left:24px;top:54px;font-family:Georgia,"Times New Roman",serif;font-size:18px;font-weight:600}
.info-row{position:absolute;left:24px;display:flex;align-items:center;gap:12px;font-size:13px}
.field{position:absolute;border-bottom:1px solid #222;font-size:11px;padding-bottom:14px}
.submit{position:absolute;left:353px;top:245px;width:556px;height:28px;border-radius:14px;background:var(--orange);color:var(--white);font-size:13px;display:flex;align-items:center;justify-content:center}

/* footer */
.footer{position:absolute;left:0;top:3763px;width:1200px;height:349px;background:var(--footer)}
.footer-art{position:absolute;inset:0;background:radial-gradient(circle at 55% 45%,#4f86a8 0%,rgba(79,134,168,.2) 35%,rgba(94,109,121,0) 60%),linear-gradient(90deg,#7a8792 0%,#5e6d79 40%,#56636e 100%)}
.footer .brand{position:absolute;left:64px;top:60px;font-size:46px;color:var(--navy)}
.footer .about-text{position:absolute;left:60px;top:145px;width:240px;font-size:11.5px;line-height:20px;color:var(--white)}
.links{position:absolute;color:var(--white);font-size:12px;line-height:34px}
.links h6{font-size:12px;font-weight:600;letter-spacing:.5px}
.copy{position:absolute;left:61px;top:251px;width:1079px;height:51px;border-radius:26px;background:rgba(232,236,239,.85);display:flex;align-items:center;justify-content:space-between;padding:0 32px;font-size:10.5px;font-weight:600;color:var(--white)}
.social{display:flex;gap:12px}
.social span{width:26px;height:26px;border-radius:6px;background:var(--white)}
</style>
</head>
<body>

<!-- HERO -->
<header class="hero">
  <div class="hero-photo" role="img" aria-label="Smiling nurse in teal scrubs comforting an elderly woman in a white robe seated in a wheelchair"></div>
  <div class="brand abs" style="left:64px;top:32px;font-size:28px"><span class="dot"></span>Velora Health</div>
  <nav class="nav">
    <a class="active" href="#">Home</a><a href="#">About Us</a><a href="#">Services</a><a href="#">Meet Our Team</a><a href="#">Testimonials</a>
  </nav>
  <a class="btn" style="left:977px;top:26px;width:163px;height:44px;border-radius:22px">Book an Appointment</a>

  <h1>Compassionate Care<br>for Mental Wellness</h1>
  <p class="sub">Restoring Hope One Mind at a Time</p>
  <p class="lead">Lorem ipsum dolor sit amet, consectetur adipiscing elit, sed do eiusmod tempor incididunt ut labore et dolore magna aliqua. Ut enim ad minim veniam, quis nostrud</p>
  <a class="btn" style="left:64px;top:487px;width:163px;height:41px">Book an Appointment</a>

  <div class="stat stat-care">
    <div class="faces"><span></span><span></span><span></span><span></span></div>
    <div><b>150k +</b><small>customer care</small></div>
  </div>
  <svg class="tick" viewBox="0 0 22 22"><circle cx="11" cy="11" r="11" fill="#102a43"/><path d="M6 11.5l3.2 3.2L16 8" stroke="#fff" stroke-width="2" fill="none"/></svg>

  <div class="stat stat-doc">
    <div class="faces" style="margin-left:8px"><span style="width:22px;height:22px"></span><span style="width:22px;height:22px"></span><span style="width:22px;height:22px"></span><span style="width:22px;height:22px"></span></div>
    <b>800+</b><small>DOCTORS</small>
  </div>
</header>

<!-- ABOUT -->
<section class="about">
  <p class="eyebrow">ABOUT US</p>
  <h2>Mental Health Support<br>Rooted in Understanding</h2>
  <div class="photo" style="left:62px;top:997px;width:528px;height:374px;background:linear-gradient(180deg,#8fd0d6 0%,#e6f2f2 40%,#f1f1ef 100%)" role="img" aria-label="Caregiver embracing an elderly woman seated on a sofa"></div>
  <div class="photo" style="left:611px;top:803px;width:529px;height:373px;background:linear-gradient(120deg,#f2f3f2 0%,#d9dcdc 45%,#8aa6c4 70%,#3b3b40 100%)" role="img" aria-label="Young man on a grey couch talking with a therapist holding a clipboard"></div>
  <p class="body-text abs" style="left:621px;top:1201px;width:300px">Lorem ipsum dolor sit amet, consectetur adipiscing elit, sed do eiusmod tempor incididunt ut labore et dolore magna aliqua. Ut enim ad minim veniam, quis</p>
  <a class="btn" style="left:621px;top:1283px;width:113px;height:29px">Explore More</a>
</section>

<!-- SERVICES -->
<section class="band" style="top:1468px;height:620px"></section>
<p class="band-title" style="top:1514px;font-size:24px;letter-spacing:4px">SERVICES</p>
<p class="band-title" style="top:1570px;font-size:32px;letter-spacing:4px">Comprehensive Care For Every Mind.</p>

<article class="svc" style="left:59px">
  <div class="img" style="background:linear-gradient(135deg,#d8dcdf,#8a9aa8)" role="img" aria-label="Therapist and client talking in an individual session"></div>
  <div class="head"><span class="icon"><svg width="22" height="22" viewBox="0 0 22 22" fill="none" stroke="#102a43" stroke-width="1.5"><circle cx="11" cy="6" r="3"/><path d="M5 20v-5a6 6 0 0112 0v5"/></svg></span>Individual Therapy</div>
  <div class="rule"></div>
  <p>Lorem ipsum dolor sit amet, consectetur adipiscing elit, sed do eiusmod tempor incididunt ut</p>
  <a class="btn">Learn More</a>
</article>
<article class="svc featured" style="left:333px">
  <div class="img" style="background:linear-gradient(135deg,#b59a86,#e7ddd3)" role="img" aria-label="Family sitting together on a sofa during counseling"></div>
  <div class="head"><span class="icon"><svg width="22" height="22" viewBox="0 0 22 22" fill="none" stroke="#102a43" stroke-width="1.5"><circle cx="7" cy="7" r="2.5"/><circle cx="15" cy="7" r="2.5"/><path d="M2 19v-3a5 5 0 0110 0v3M10 19v-3a5 5 0 0110 0v3"/></svg></span>Family Counseling</div>
  <div class="rule"></div>
  <p>Lorem ipsum dolor sit amet, consectetur adipiscing elit, sed do eiusmod tempor incididunt ut</p>
  <a class="btn orange">Learn More</a>
</article>
<article class="svc" style="left:607px">
  <div class="img" style="background:linear-gradient(135deg,#f2f2f0,#b7c0c4)" role="img" aria-label="Doctor waving to a patient on a laptop video call"></div>
  <div class="head"><span class="icon"><svg width="22" height="22" viewBox="0 0 22 22" fill="none" stroke="#102a43" stroke-width="1.5"><rect x="3" y="4" width="16" height="11" rx="1"/><path d="M7 19h8"/></svg></span>Tele Health</div>
  <div class="rule"></div>
  <p>Lorem ipsum dolor sit amet, consectetur adipiscing elit, sed do eiusmod tempor incididunt ut</p>
  <a class="btn">Learn More</a>
</article>
<article class="svc" style="left:881px">
  <div class="img" style="background:linear-gradient(135deg,#e4e4e2,#8d857f)" role="img" aria-label="Psychiatrist consoling a distressed woman on a couch"></div>
  <div class="head"><span class="icon"><svg width="22" height="22" viewBox="0 0 22 22" fill="none" stroke="#102a43" stroke-width="1.5"><circle cx="11" cy="9" r="6"/><path d="M4 19c2-2 12-2 14 0"/></svg></span>Psychiatry</div>
  <div class="rule"></div>
  <p>Lorem ipsum dolor sit amet, consectetur adipiscing elit, sed do eiusmod tempor incididunt ut</p>
  <a class="btn">Learn More</a>
</article>

<!-- TEAM -->
<p class="section-label" style="top:2193px;font-size:26px;font-weight:400">OUR TEAM</p>
<h2 class="section-label" style="top:2249px;font-size:32px">Meet The People Who Make Healing Possible</h2>

<article class="member" style="left:59px"><div class="band-top"></div><div class="avatar" role="img" aria-label="Portrait of a doctor in a white coat"></div><h3>Mara Ellison</h3><p>Lorem ipsum dolor sit amet, consectetur adipiscing elit, sed do eiusmod tempor incididunt ut</p><div class="more">Learn More <svg width="26" height="10" viewBox="0 0 26 10" fill="none" stroke="#f37f23" stroke-width="1.5"><path d="M0 5h24M20 1l4 4-4 4"/></svg></div></article>
<article class="member" style="left:333px"><div class="band-top"></div><div class="avatar" role="img" aria-label="Portrait of a medical team"></div><h3>Tobin Reyes</h3><p>Lorem ipsum dolor sit amet, consectetur adipiscing elit, sed do eiusmod tempor incididunt ut</p><div class="more">Learn More <svg width="26" height="10" viewBox="0 0 26 10" fill="none" stroke="#f37f23" stroke-width="1.5"><path d="M0 5h24M20 1l4 4-4 4"/></svg></div></article>
<article class="member" style="left:607px"><div class="band-top"></div><div class="avatar" role="img" aria-label="Portrait of a group of clinicians"></div><h3>Lena Okafor</h3><p>Lorem ipsum dolor sit amet, consectetur adipiscing elit, sed do eiusmod tempor incididunt ut</p><div class="more">Learn More <svg width="26" height="10" viewBox="0 0 26 10" fill="none" stroke="#f37f23" stroke-width="1.5"><path d="M0 5h24M20 1l4 4-4 4"/></svg></div></article>
<article class="member" style="left:881px"><div class="band-top"></div><div class="avatar" role="img" aria-label="Portrait of a nurse in teal scrubs"></div><h3>Corin Vale</h3><p>Lorem ipsum dolor sit amet, consectetur adipiscing elit, sed do eiusmod tempor incididunt ut</p><div class="more">Learn More <svg width="26" height="10" viewBox="0 0 26 10" fill="none" stroke="#f37f23" stroke-width="1.5"><path d="M0 5h24M20 1l4 4-4 4"/></svg></div></article>

<!-- TESTIMONIALS -->
<section class="band" style="top:2710px;height:426px"></section>
<p class="band-title" style="top:2766px;font-size:26px;letter-spacing:1px">TESTIMONIALS</p>
<p class="band-title" style="top:2826px;font-size:33px;letter-spacing:1px">Trusted By Thousands Loved By Many</p>

<article class="review" style="left:126px">
  <p>Lorem ipsum dolor sit amet, consectetur adipiscing elit, sed do eiusmod tempor incididunt ut labore et dolore magna aliqua. Ut enim ad minim veniam, quis</p>
  <div class="who"><div class="pic" role="img" aria-label="Client portrait"></div><div><h4>Mara Ellison</h4><small>Heir Guidance Helped Me<br>Double My Productivity.</small></div></div>
  <div class="stars">★★★★★</div>
</article>
<article class="review" style="left:634px">
  <p>Lorem ipsum dolor sit amet, consectetur adipiscing elit, sed do eiusmod tempor incididunt ut labore et dolore magna aliqua. Ut enim ad minim veniam, quis</p>
  <div class="who"><div class="pic" role="img" aria-label="Client portrait"></div><div><h4>Mara Ellison</h4><small>Heir Guidance Helped Me<br>Double My Productivity.</small></div></div>
  <div class="stars">★★★★★</div>
</article>

<!-- CONTACT -->
<p class="section-label" style="top:3238px;font-size:26px;font-weight:400">CONTACT US</p>
<h2 class="section-label" style="top:3292px;font-size:32px;font-weight:400">"Get In Touch With Our Team Today</h2>

<section class="contact-box">
  <div class="contact-info">
    <h5>info</h5>
    <div class="info-row" style="top:110px"><svg width="18" height="18" viewBox="0 0 18 18" fill="none" stroke="#fff" stroke-width="1.3"><path d="M4 2l3 3-2 2a10 10 0 006 6l2-2 3 3-2 2C7 16 2 11 2 4z"/></svg>(202) 555-0147</div>
    <div class="info-row" style="top:155px"><svg width="18" height="14" viewBox="0 0 18 14" fill="none" stroke="#fff" stroke-width="1.3"><rect x="1" y="1" width="16" height="12"/><path d="M1 1l8 7 8-7"/></svg>care@velorahealth.com</div>
    <div class="info-row" style="top:200px"><svg width="16" height="18" viewBox="0 0 16 18" fill="none" stroke="#fff" stroke-width="1.3"><path d="M8 17s6-6 6-10A6 6 0 002 7c0 4 6 10 6 10z"/><circle cx="8" cy="7" r="2"/></svg>1420 Harlow Street NW,</div>
    <div class="info-row" style="top:240px;font-family:Georgia,serif;font-size:11px;gap:20px">Social Media
      <span style="display:flex;gap:6px"><i style="width:10px;height:10px;border:1.2px solid #fff;display:block"></i><i style="width:10px;height:10px;border:1.2px solid #fff;display:block"></i><i style="width:10px;height:10px;border:1.2px solid #fff;display:block"></i><i style="width:10px;height:10px;border:1.2px solid #fff;border-radius:50%;display:block"></i></span>
    </div>
  </div>
  <div class="field" style="left:356px;top:30px;width:259px">Name</div>
  <div class="field" style="left:653px;top:30px;width:259px">Phone</div>
  <div class="field" style="left:356px;top:100px;width:259px">Email</div>
  <div class="field" style="left:653px;top:100px;width:259px">Adress</div>
  <div class="field" style="left:352px;top:170px;width:560px;padding-bottom:18px">Message</div>
  <div class="submit">Submit</div>
</section>

<!-- FOOTER -->
<footer class="footer">
  <div class="footer-art" role="img" aria-label="Faint hexagon pattern of medical icons over a blurred clinic background"></div>
  <div class="brand"><span class="dot" style="width:16px;height:16px"></span>Velora Health</div>
  <p class="about-text">Lorem ipsum dolor sit amet, consectetur adipiscing elit, sed do eiusmod tempor incididunt ut labore et</p>
  <div class="links" style="left:855px;top:30px;line-height:34px">
    <h6>QUICK LINKS</h6>
    <div>Home</div><div>About Us</div><div>Services</div><div>Meet Our Team</div><div>Testimonials</div>
  </div>
  <div class="links" style="left:1052px;top:28px;line-height:40px;font-size:13px">
    <h6 style="font-size:18px;font-weight:400">Legal</h6>
    <div>Privacy Policy</div><div>Terms Of Use</div><div>Cookie Policy</div>
  </div>
  <div class="copy">
    <span>Copyright © 2025. All Rights Reserved.</span>
    <div class="social"><span></span><span style="border-radius:8px"></span><span></span><span style="border-radius:50%"></span></div>
  </div>
</footer>

</body>
</html>
```